2014 Wall Calendar Needed

I need a 2014 wall calendar design tweaked for my business Brindle Building Advisors. We are a construction scheduling company you can check out our website www.advisebrindle.example . I had calendars designed last year (attachment #1) that I was pretty happy with but need the following improvements:

1. The Colors on the calendar and the logo must match - Notice the blue on the calendar and the blue on the header are different.

2. The calendar must contain at least 2, preferably 3 months from the end of 2013, and the beginning of 2015. (Some suggested layouts in Attachment #2 and #3)

3. The calendar must have out new "cloud" logo (Attachment #4) and website URL: cloud.advisebrindle.example

4. The calendar should contain the original logo (attachment #5) , and verbiage somewhere:
BRINDLE Building Advisors; Project Solutions; Scheduling, Earned Value Management, Dispute Resolution, 4D Scheduling, Application Cloud Solutions;

5. The contact information:
4372 Harlow Street Suite 500
Silver Spring, MD 20910
Phone 301 555 7186
www.advisebrindle.example

6. The calendar should highlight week numbers and all major American and religious holidays (the holidays on the current calendar are more than enough, as are the week numbers)
Updates

The attachments have been uploaded. Additionally, you cal follow this link to download the attachments referenced in the posting.

 LINK-> https://advisebrindle.filedrop.example/d/k7q2w9184503726615 
 

Target Market(s)

This poster will be sitting in a construction manager's office on the wall and will be used for "at a glance" planning

Industry/Entity Type

Construction

Requirements
Must have
• 1. Contact Information
2. Brindle Logo (attachment #5
3. Brindle Cloud Logo (Attachment #4)
4. 2014 Calendar year
5. at least 2, preferrably 3 months from the surrounding years (Oct Nov Dec 2013 and Jan Feb March of 2015)
6. Major American and Religious holidays
7. Must be able to print on standard poster size: 24X36 INCHES etc.
Nice to have
• Under each month in small font, I would like to have "anticipated weather days *" followed by a number. This number will indicate the anticipated days of inclement weather. I WILL RESEARCH SUPPLY THESE NUMBERS AFTER I CHOOSE THE FINAL DESIGN, these numbers will range from 1-10. At the bottom of the calendar will be an asterisk (*) which references the above statement and reads: "these estimates based on 5 day workweek in the Washington DC/VA area - may vary from contract to contract" this should also be in small font.

```html
<!DOCTYPE html>
<html lang="en">
<head>
<meta charset="utf-8">
<title>Brindle Building Advisors – 2014 Wall Calendar</title>
<link href="https://fonts.googleapis.com/css2?family=Open+Sans:wght@400;600;700;800&display=swap" rel="stylesheet">
<style>
:root{
  --blue:#1b8ad6;
  --blue-dark:#146fb0;
  --pale:#dcedf9;
  --hol:#a9d4f2;
  --ink:#2a3440;
  --grey:#7b8794;
  --white:#ffffff;
}
*{box-sizing:border-box;margin:0;padding:0}
html,body{width:841px;height:1200px;overflow:hidden;background:var(--white)}
body{font-family:"Open Sans",Arial,sans-serif;color:var(--ink)}
.canvas{position:relative;width:841px;height:1200px;overflow:hidden;background:var(--white)}

.brand{position:absolute;left:14px;top:14px;display:flex;align-items:center;gap:10px}
.brand-square{width:40px;height:40px;background:var(--blue)}
.brand-name{color:var(--blue);font-weight:700;line-height:1}
.brand-name .big{display:block;font-size:32px;letter-spacing:1px}
.brand-name .small{display:block;font-size:11.5px;letter-spacing:1.6px;margin-top:4px;text-transform:uppercase}

.year{position:absolute;right:12px;top:-6px;font-size:116px;font-weight:800;color:var(--blue);letter-spacing:4px;line-height:1.1}

.month{position:absolute;width:198px}
.mhead{display:flex;justify-content:space-between;align-items:baseline;background:var(--pale);border-bottom:2px solid var(--blue);padding:2px 6px 1px;color:var(--blue);font-weight:700}
.mhead .name{font-size:14px}
.mhead .yr{font-size:11px}
.cal{width:100%;border-collapse:collapse;table-layout:fixed;font-size:10px}
.cal col.wk{width:21px}
.cal thead td{font-size:7.5px;color:var(--grey);height:13px;font-weight:600}
.cal td{text-align:center;height:16px;border-bottom:1px solid var(--pale)}
.cal th{background:var(--pale);color:var(--blue);font-size:8px;font-weight:700;border-bottom:1px solid var(--white)}
.cal td.hol{background:var(--hol);font-weight:700;color:var(--blue-dark)}
.weather{font-size:9px;color:var(--blue);font-weight:600;padding:2px 0 0 24px}

.holidays{position:absolute;left:12px;top:990px;width:506px;border:1px solid var(--blue)}
.holidays h2{background:var(--blue);color:var(--white);font-size:9px;font-weight:700;text-align:center;padding:2px 0}
.holidays ul{list-style:none;columns:3;column-gap:8px;padding:4px 6px;font-size:7.5px;line-height:9.6px}
.holidays li b{color:var(--blue);display:inline-block;width:42px}

.note{position:absolute;left:530px;top:994px;width:94px;font-size:7.5px;line-height:10px;color:var(--ink);display:flex;gap:4px}
.note .star{color:var(--blue);font-size:26px;font-weight:800;line-height:22px}

.cloud{position:absolute;left:633px;top:850px;width:198px;display:flex;flex-direction:column;align-items:center;gap:6px}
.cloud-mark{display:flex;align-items:center;gap:8px}
.cloud-circle{width:40px;height:40px;border-radius:50%;background:var(--blue)}
.cloud-name{color:var(--blue);font-weight:700;font-size:24px}
.cloud-url{font-size:10px;color:var(--blue);font-weight:600}

.contact{position:absolute;left:633px;top:960px;width:198px;text-align:center;font-size:10.5px;line-height:15px;color:var(--ink)}
.contact .lbl{color:var(--blue);font-weight:700}

.band{position:absolute;left:0;top:1092px;width:841px;height:108px;background:var(--blue);color:var(--white);display:flex;flex-direction:column;justify-content:center;align-items:center;gap:10px;font-size:14px;font-weight:600}
.band p{display:flex;align-items:center;gap:12px}
.band i{display:inline-block;width:8px;height:8px;background:var(--white)}
</style>
</head>
<body>
<div class="canvas">

  <div class="brand">
    <span class="brand-square"></span>
    <div class="brand-name"><span class="big">BRINDLE</span><span class="small">Building Advisors</span></div>
  </div>
  <div class="year">2014</div>

  <!-- Row 0 -->
  <div class="month" style="left:219px;top:128px">
    <div class="mhead"><span class="name">October</span><span class="yr">2013</span></div>
    <table class="cal"><colgroup><col class="wk"><col span="7"></colgroup>
      <thead><tr><td></td><td>Sun</td><td>Mon</td><td>Tue</td><td>Wed</td><td>Thu</td><td>Fri</td><td>Sat</td></tr></thead>
      <tbody>
        <tr><th>40</th><td></td><td></td><td>1</td><td>2</td><td>3</td><td>4</td><td>5</td></tr>
        <tr><th>41</th><td>6</td><td>7</td><td>8</td><td>9</td><td>10</td><td>11</td><td>12</td></tr>
        <tr><th>42</th><td>13</td><td class="hol">14</td><td>15</td><td>16</td><td>17</td><td>18</td><td>19</td></tr>
        <tr><th>43</th><td>20</td><td>21</td><td>22</td><td>23</td><td>24</td><td>25</td><td>26</td></tr>
        <tr><th>44</th><td>27</td><td>28</td><td>29</td><td>30</td><td>31</td><td></td><td></td></tr>
      </tbody></table>
    <div class="weather">*3</div>
  </div>
  <div class="month" style="left:426px;top:128px">
    <div class="mhead"><span class="name">November</span><span class="yr">2013</span></div>
    <table class="cal"><colgroup><col class="wk"><col span="7"></colgroup>
      <thead><tr><td></td><td>Sun</td><td>Mon</td><td>Tue</td><td>Wed</td><td>Thu</td><td>Fri</td><td>Sat</td></tr></thead>
      <tbody>
        <tr><th>44</th><td></td><td></td><td></td><td></td><td></td><td>1</td><td>2</td></tr>
        <tr><th>45</th><td>3</td><td>4</td><td>5</td><td>6</td><td>7</td><td>8</td><td>9</td></tr>
        <tr><th>46</th><td>10</td><td class="hol">11</td><td>12</td><td>13</td><td>14</td><td>15</td><td>16</td></tr>
        <tr><th>47</th><td>17</td><td>18</td><td>19</td><td>20</td><td>21</td><td>22</td><td>23</td></tr>
        <tr><th>48</th><td>24</td><td>25</td><td>26</td><td>27</td><td class="hol">28</td><td>29</td><td>30</td></tr>
      </tbody></table>
    <div class="weather">*4</div>
  </div>
  <div class="month" style="left:633px;top:128px">
    <div class="mhead"><span class="name">December</span><span class="yr">2013</span></div>
    <table class="cal"><colgroup><col class="wk"><col span="7"></colgroup>
      <thead><tr><td></td><td>Sun</td><td>Mon</td><td>Tue</td><td>Wed</td><td>Thu</td><td>Fri</td><td>Sat</td></tr></thead>
      <tbody>
        <tr><th>49</th><td>1</td><td>2</td><td>3</td><td>4</td><td>5</td><td>6</td><td>7</td></tr>
        <tr><th>50</th><td>8</td><td>9</td><td>10</td><td>11</td><td>12</td><td>13</td><td>14</td></tr>
        <tr><th>51</th><td>15</td><td>16</td><td>17</td><td>18</td><td>19</td><td>20</td><td>21</td></tr>
        <tr><th>52</th><td>22</td><td>23</td><td>24</td><td class="hol">25</td><td>26</td><td>27</td><td>28</td></tr>
        <tr><th>1</th><td>29</td><td>30</td><td>31</td><td></td><td></td><td></td><td></td></tr>
      </tbody></table>
    <div class="weather">*6</div>
  </div>

  <!-- Row 1 -->
  <div class="month" style="left:12px;top:306px">
    <div class="mhead"><span class="name">January</span><span class="yr">2014</span></div>
    <table class="cal"><colgroup><col class="wk"><col span="7"></colgroup>
      <thead><tr><td></td><td>Sun</td><td>Mon</td><td>Tue</td><td>Wed</td><td>Thu</td><td>Fri</td><td>Sat</td></tr></thead>
      <tbody>
        <tr><th>1</th><td></td><td></td><td></td><td class="hol">1</td><td>2</td><td>3</td><td>4</td></tr>
        <tr><th>2</th><td>5</td><td>6</td><td>7</td><td>8</td><td>9</td><td>10</td><td>11</td></tr>
        <tr><th>3</th><td>12</td><td>13</td><td>14</td><td>15</td><td>16</td><td>17</td><td>18</td></tr>
        <tr><th>4</th><td>19</td><td class="hol">20</td><td>21</td><td>22</td><td>23</td><td>24</td><td>25</td></tr>
        <tr><th>5</th><td>26</td><td>27</td><td>28</td><td>29</td><td>30</td><td>31</td><td></td></tr>
      </tbody></table>
    <div class="weather">*8</div>
  </div>
  <div class="month" style="left:219px;top:306px">
    <div class="mhead"><span class="name">February</span><span class="yr">2014</span></div>
    <table class="cal"><colgroup><col class="wk"><col span="7"></colgroup>
      <thead><tr><td></td><td>Sun</td><td>Mon</td><td>Tue</td><td>Wed</td><td>Thu</td><td>Fri</td><td>Sat</td></tr></thead>
      <tbody>
        <tr><th>5</th><td></td><td></td><td></td><td></td><td></td><td></td><td>1</td></tr>
        <tr><th>6</th><td>2</td><td>3</td><td>4</td><td>5</td><td>6</td><td>7</td><td>8</td></tr>
        <tr><th>7</th><td>9</td><td>10</td><td>11</td><td>12</td><td>13</td><td class="hol">14</td><td>15</td></tr>
        <tr><th>8</th><td>16</td><td class="hol">17</td><td>18</td><td>19</td><td>20</td><td>21</td><td>22</td></tr>
        <tr><th>9</th><td>23</td><td>24</td><td>25</td><td>26</td><td>27</td><td>28</td><td></td></tr>
      </tbody></table>
    <div class="weather">*7</div>
  </div>
  <div class="month" style="left:426px;top:306px">
    <div class="mhead"><span class="name">March</span><span class="yr">2014</span></div>
    <table class="cal"><colgroup><col class="wk"><col span="7"></colgroup>
      <thead><tr><td></td><td>Sun</td><td>Mon</td><td>Tue</td><td>Wed</td><td>Thu</td><td>Fri</td><td>Sat</td></tr></thead>
      <tbody>
        <tr><th>9</th><td></td><td></td><td></td><td></td><td></td><td></td><td>1</td></tr>
        <tr><th>10</th><td>2</td><td>3</td><td>4</td><td class="hol">5</td><td>6</td><td>7</td><td>8</td></tr>
        <tr><th>11</th><td>9</td><td>10</td><td>11</td><td>12</td><td>13</td><td>14</td><td>15</td></tr>
        <tr><th>12</th><td>16</td><td>17</td><td>18</td><td>19</td><td>20</td><td>21</td><td>22</td></tr>
        <tr><th>13</th><td>23</td><td>24</td><td>25</td><td>26</td><td>27</td><td>28</td><td>29</td></tr>
        <tr><th>14</th><td>30</td><td>31</td><td></td><td></td><td></td><td></td><td></td></tr>
      </tbody></table>
    <div class="weather">*5</div>
  </div>
  <div class="month" style="left:633px;top:306px">
    <div class="mhead"><span class="name">April</span><span class="yr">2014</span></div>
    <table class="cal"><colgroup><col class="wk"><col span="7"></colgroup>
      <thead><tr><td></td><td>Sun</td><td>Mon</td><td>Tue</td><td>Wed</td><td>Thu</td><td>Fri</td><td>Sat</td></tr></thead>
      <tbody>
        <tr><th>14</th><td></td><td></td><td>1</td><td>2</td><td>3</td><td>4</td><td>5</td></tr>
        <tr><th>15</th><td>6</td><td>7</td><td>8</td><td>9</td><td>10</td><td>11</td><td>12</td></tr>
        <tr><th>16</th><td>13</td><td>14</td><td class="hol">15</td><td>16</td><td>17</td><td class="hol">18</td><td>19</td></tr>
        <tr><th>17</th><td class="hol">20</td><td>21</td><td>22</td><td>23</td><td>24</td><td>25</td><td>26</td></tr>
        <tr><th>18</th><td>27</td><td>28</td><td>29</td><td>30</td><td></td><td></td><td></td></tr>
      </tbody></table>
    <div class="weather">*4</div>
  </div>

  <!-- Row 2 -->
  <div class="month" style="left:12px;top:484px">
    <div class="mhead"><span class="name">May</span><span class="yr">2014</span></div>
    <table class="cal"><colgroup><col class="wk"><col span="7"></colgroup>
      <thead><tr><td></td><td>Sun</td><td>Mon</td><td>Tue</td><td>Wed</td><td>Thu</td><td>Fri</td><td>Sat</td></tr></thead>
      <tbody>
        <tr><th>18</th><td></td><td></td><td></td><td></td><td>1</td><td>2</td><td>3</td></tr>
        <tr><th>19</th><td>4</td><td>5</td><td>6</td><td>7</td><td>8</td><td>9</td><td>10</td></tr>
        <tr><th>20</th><td class="hol">11</td><td>12</td><td>13</td><td>14</td><td>15</td><td>16</td><td>17</td></tr>
        <tr><th>21</th><td>18</td><td>19</td><td>20</td><td>21</td><td>22</td><td>23</td><td>24</td></tr>
        <tr><th>22</th><td>25</td><td class="hol">26</td><td>27</td><td>28</td><td>29</td><td>30</td><td>31</td></tr>
      </tbody></table>
    <div class="weather">*4</div>
  </div>
  <div class="month" style="left:219px;top:484px">
    <div class="mhead"><span class="name">June</span><span class="yr">2014</span></div>
    <table class="cal"><colgroup><col class="wk"><col span="7"></colgroup>
      <thead><tr><td></td><td>Sun</td><td>Mon</td><td>Tue</td><td>Wed</td><td>Thu</td><td>Fri</td><td>Sat</td></tr></thead>
      <tbody>
        <tr><th>23</th><td>1</td><td>2</td><td>3</td><td>4</td><td>5</td><td>6</td><td>7</td></tr>
        <tr><th>24</th><td>8</td><td>9</td><td>10</td><td>11</td><td>12</td><td>13</td><td>14</td></tr>
        <tr><th>25</th><td class="hol">15</td><td>16</td><td>17</td><td>18</td><td>19</td><td>20</td><td>21</td></tr>
        <tr><th>26</th><td>22</td><td>23</td><td>24</td><td>25</td><td>26</td><td>27</td><td>28</td></tr>
        <tr><th>27</th><td>29</td><td>30</td><td></td><td></td><td></td><td></td><td></td></tr>
      </tbody></table>
    <div class="weather">*3</div>
  </div>
  <div class="month" style="left:426px;top:484px">
    <div class="mhead"><span class="name">July</span><span class="yr">2014</span></div>
    <table class="cal"><colgroup><col class="wk"><col span="7"></colgroup>
      <thead><tr><td></td><td>Sun</td><td>Mon</td><td>Tue</td><td>Wed</td><td>Thu</td><td>Fri</td><td>Sat</td></tr></thead>
      <tbody>
        <tr><th>27</th><td></td><td></td><td>1</td><td>2</td><td>3</td><td class="hol">4</td><td>5</td></tr>
        <tr><th>28</th><td>6</td><td>7</td><td>8</td><td>9</td><td>10</td><td>11</td><td>12</td></tr>
        <tr><th>29</th><td>13</td><td>14</td><td>15</td><td>16</td><td>17</td><td>18</td><td>19</td></tr>
        <tr><th>30</th><td>20</td><td>21</td><td>22</td><td>23</td><td>24</td><td>25</td><td>26</td></tr>
        <tr><th>31</th><td>27</td><td>28</td><td>29</td><td>30</td><td>31</td><td></td><td></td></tr>
      </tbody></table>
    <div class="weather">*3</div>
  </div>
  <div class="month" style="left:633px;top:484px">
    <div class="mhead"><span class="name">August</span><span class="yr">2014</span></div>
    <table class="cal"><colgroup><col class="wk"><col span="7"></colgroup>
      <thead><tr><td></td><td>Sun</td><td>Mon</td><td>Tue</td><td>Wed</td><td>Thu</td><td>Fri</td><td>Sat</td></tr></thead>
      <tbody>
        <tr><th>31</th><td></td><td></td><td></td><td></td><td></td><td>1</td><td>2</td></tr>
        <tr><th>32</th><td>3</td><td>4</td><td>5</td><td>6</td><td>7</td><td>8</td><td>9</td></tr>
        <tr><th>33</th><td>10</td><td>11</td><td>12</td><td>13</td><td>14</td><td>15</td><td>16</td></tr>
        <tr><th>34</th><td>17</td><td>18</td><td>19</td><td>20</td><td>21</td><td>22</td><td>23</td></tr>
        <tr><th>35</th><td>24</td><td>25</td><td>26</td><td>27</td><td>28</td><td>29</td><td>30</td></tr>
        <tr><th>36</th><td>31</td><td></td><td></td><td></td><td></td><td></td><td></td></tr>
      </tbody></table>
    <div class="weather">*2</div>
  </div>

  <!-- Row 3 -->
  <div class="month" style="left:12px;top:662px">
    <div class="mhead"><span class="name">September</span><span class="yr">2014</span></div>
    <table class="cal"><colgroup><col class="wk"><col span="7"></colgroup>
      <thead><tr><td></td><td>Sun</td><td>Mon</td><td>Tue</td><td>Wed</td><td>Thu</td><td>Fri</td><td>Sat</td></tr></thead>
      <tbody>
        <tr><th>36</th><td></td><td class="hol">1</td><td>2</td><td>3</td><td>4</td><td>5</td><td>6</td></tr>
        <tr><th>37</th><td>7</td><td>8</td><td>9</td><td>10</td><td>11</td><td>12</td><td>13</td></tr>
        <tr><th>38</th><td>14</td><td>15</td><td>16</td><td>17</td><td>18</td><td>19</td><td>20</td></tr>
        <tr><th>39</th><td>21</td><td>22</td><td>23</td><td>24</td><td class="hol">25</td><td>26</td><td>27</td></tr>
        <tr><th>40</th><td>28</td><td>29</td><td>30</td><td></td><td></td><td></td><td></td></tr>
      </tbody></table>
    <div class="weather">*3</div>
  </div>
  <div class="month" style="left:219px;top:662px">
    <div class="mhead"><span class="name">October</span><span class="yr">2014</span></div>
    <table class="cal"><colgroup><col class="wk"><col span="7"></colgroup>
      <thead><tr><td></td><td>Sun</td><td>Mon</td><td>Tue</td><td>Wed</td><td>Thu</td><td>Fri</td><td>Sat</td></tr></thead>
      <tbody>
        <tr><th>40</th><td></td><td></td><td></td><td>1</td><td>2</td><td>3</td><td class="hol">4</td></tr>
        <tr><th>41</th><td>5</td><td>6</td><td>7</td><td>8</td><td>9</td><td>10</td><td>11</td></tr>
        <tr><th>42</th><td>12</td><td class="hol">13</td><td>14</td><td>15</td><td>16</td><td>17</td><td>18</td></tr>
        <tr><th>43</th><td>19</td><td>20</td><td>21</td><td>22</td><td>23</td><td>24</td><td>25</td></tr>
        <tr><th>44</th><td>26</td><td>27</td><td>28</td><td>29</td><td>30</td><td>31</td><td></td></tr>
      </tbody></table>
    <div class="weather">*3</div>
  </div>
  <div class="month" style="left:426px;top:662px">
    <div class="mhead"><span class="name">November</span><span class="yr">2014</span></div>
    <table class="cal"><colgroup><col class="wk"><col span="7"></colgroup>
      <thead><tr><td></td><td>Sun</td><td>Mon</td><td>Tue</td><td>Wed</td><td>Thu</td><td>Fri</td><td>Sat</td></tr></thead>
      <tbody>
        <tr><th>44</th><td></td><td></td><td></td><td></td><td></td><td></td><td>1</td></tr>
        <tr><th>45</th><td>2</td><td>3</td><td>4</td><td>5</td><td>6</td><td>7</td><td>8</td></tr>
        <tr><th>46</th><td>9</td><td>10</td><td class="hol">11</td><td>12</td><td>13</td><td>14</td><td>15</td></tr>
        <tr><th>47</th><td>16</td><td>17</td><td>18</td><td>19</td><td>20</td><td>21</td><td>22</td></tr>
        <tr><th>48</th><td>23</td><td>24</td><td>25</td><td>26</td><td class="hol">27</td><td>28</td><td>29</td></tr>
        <tr><th>49</th><td>30</td><td></td><td></td><td></td><td></td><td></td><td></td></tr>
      </tbody></table>
    <div class="weather">*4</div>
  </div>
  <div class="month" style="left:633px;top:662px">
    <div class="mhead"><span class="name">December</span><span class="yr">2014</span></div>
    <table class="cal"><colgroup><col class="wk"><col span="7"></colgroup>
      <thead><tr><td></td><td>Sun</td><td>Mon</td><td>Tue</td><td>Wed</td><td>Thu</td><td>Fri</td><td>Sat</td></tr></thead>
      <tbody>
        <tr><th>49</th><td></td><td>1</td><td>2</td><td>3</td><td>4</td><td>5</td><td>6</td></tr>
        <tr><th>50</th><td>7</td><td>8</td><td>9</td><td>10</td><td>11</td><td>12</td><td>13</td></tr>
        <tr><th>51</th><td>14</td><td>15</td><td>16</td><td class="hol">17</td><td>18</td><td>19</td><td>20</td></tr>
        <tr><th>52</th><td>21</td><td>22</td><td>23</td><td>24</td><td class="hol">25</td><td>26</td><td>27</td></tr>
        <tr><th>1</th><td>28</td><td>29</td><td>30</td><td>31</td><td></td><td></td><td></td></tr>
      </tbody></table>
    <div class="weather">*6</div>
  </div>

  <!-- Row 4 -->
  <div class="month" style="left:12px;top:840px">
    <div class="mhead"><span class="name">January</span><span class="yr">2015</span></div>
    <table class="cal"><colgroup><col class="wk"><col span="7"></colgroup>
      <thead><tr><td></td><td>Sun</td><td>Mon</td><td>Tue</td><td>Wed</td><td>Thu</td><td>Fri</td><td>Sat</td></tr></thead>
      <tbody>
        <tr><th>1</th><td></td><td></td><td></td><td></td><td class="hol">1</td><td>2</td><td>3</td></tr>
        <tr><th>2</th><td>4</td><td>5</td><td>6</td><td>7</td><td>8</td><td>9</td><td>10</td></tr>
        <tr><th>3</th><td>11</td><td>12</td><td>13</td><td>14</td><td>15</td><td>16</td><td>17</td></tr>
        <tr><th>4</th><td>18</td><td class="hol">19</td><td>20</td><td>21</td><td>22</td><td>23</td><td>24</td></tr>
        <tr><th>5</th><td>25</td><td>26</td><td>27</td><td>28</td><td>29</td><td>30</td><td>31</td></tr>
      </tbody></table>
    <div class="weather">*8</div>
  </div>
  <div class="month" style="left:219px;top:840px">
    <div class="mhead"><span class="name">February</span><span class="yr">2015</span></div>
    <table class="cal"><colgroup><col class="wk"><col span="7"></colgroup>
      <thead><tr><td></td><td>Sun</td><td>Mon</td><td>Tue</td><td>Wed</td><td>Thu</td><td>Fri</td><td>Sat</td></tr></thead>
      <tbody>
        <tr><th>6</th><td>1</td><td>2</td><td>3</td><td>4</td><td>5</td><td>6</td><td>7</td></tr>
        <tr><th>7</th><td>8</td><td>9</td><td>10</td><td>11</td><td>12</td><td>13</td><td class="hol">14</td></tr>
        <tr><th>8</th><td>15</td><td class="hol">16</td><td>17</td><td class="hol">18</td><td>19</td><td>20</td><td>21</td></tr>
        <tr><th>9</th><td>22</td><td>23</td><td>24</td><td>25</td><td>26</td><td>27</td><td>28</td></tr>
      </tbody></table>
    <div class="weather">*7</div>
  </div>
  <div class="month" style="left:426px;top:840px">
    <div class="mhead"><span class="name">March</span><span class="yr">2015</span></div>
    <table class="cal"><colgroup><col class="wk"><col span="7"></colgroup>
      <thead><tr><td></td><td>Sun</td><td>Mon</td><td>Tue</td><td>Wed</td><td>Thu</td><td>Fri</td><td>Sat</td></tr></thead>
      <tbody>
        <tr><th>10</th><td>1</td><td>2</td><td>3</td><td>4</td><td>5</td><td>6</td><td>7</td></tr>
        <tr><th>11</th><td>8</td><td>9</td><td>10</td><td>11</td><td>12</td><td>13</td><td>14</td></tr>
        <tr><th>12</th><td>15</td><td>16</td><td>17</td><td>18</td><td>19</td><td>20</td><td>21</td></tr>
        <tr><th>13</th><td>22</td><td>23</td><td>24</td><td>25</td><td>26</td><td>27</td><td>28</td></tr>
      </tbody></table>
    <div class="weather">*5</div>
  </div>

  <div class="cloud">
    <div class="cloud-mark"><span class="cloud-circle"></span><span class="cloud-name">BRINDLE cloud</span></div>
    <div class="cloud-url">cloud.advisebrindle.example</div>
  </div>

  <div class="holidays">
    <h2>Major American and Religious Holidays</h2>
    <ul>
      <li><b>Oct 14 '13</b>Columbus Day</li>
      <li><b>Nov 11 '13</b>Veterans Day</li>
      <li><b>Nov 28 '13</b>Thanksgiving</li>
      <li><b>Dec 25 '13</b>Christmas Day</li>
      <li><b>Jan 1</b>New Year's Day</li>
      <li><b>Jan 20</b>M. L. King Jr. Day</li>
      <li><b>Feb 14</b>Valentine's Day</li>
      <li><b>Feb 17</b>Presidents' Day</li>
      <li><b>Mar 5</b>Ash Wednesday</li>
      <li><b>Apr 15</b>Passover</li>
      <li><b>Apr 18</b>Good Friday</li>
      <li><b>Apr 20</b>Easter Sunday</li>
      <li><b>May 11</b>Mother's Day</li>
      <li><b>May 26</b>Memorial Day</li>
      <li><b>Jun 15</b>Father's Day</li>
      <li><b>Jul 4</b>Independence Day</li>
      <li><b>Sep 1</b>Labor Day</li>
      <li><b>Sep 25</b>Rosh Hashanah</li>
      <li><b>Oct 4</b>Yom Kippur</li>
      <li><b>Oct 13</b>Columbus Day</li>
      <li><b>Nov 11</b>Veterans Day</li>
      <li><b>Nov 27</b>Thanksgiving</li>
      <li><b>Dec 17</b>Hanukkah</li>
      <li><b>Dec 25</b>Christmas Day</li>
    </ul>
  </div>

  <div class="note">
    <span class="star">*</span>
    <span>These estimates based on 5 day workweek in the Washington DC/VA area – may vary from contract to contract</span>
  </div>

  <div class="contact">
    4372 Harlow Street Suite 500<br>
    Silver Spring, MD 20910<br>
    <span class="lbl">Phone:</span> 301 555 7186<br>
    <span class="lbl">Web:</span> www.advisebrindle.example
  </div>

  <div class="band">
    <p><i></i>BRINDLE Building Advisors <i></i>Project Solutions <i></i>Scheduling <i></i>Earned Value Management</p>
    <p><i></i>Dispute Resolution <i></i>4D Scheduling <i></i>Application Cloud Solutions</p>
  </div>

</div>
</body>
</html>
```